Business Card Design

I have been a licensed, bonded and insured electrical contractor for 30+ years, working primarily in The Villages, Spruce Creek and surrounding areas of Central Florida. I also maintain Master Beacon Fellow designation from the National Fixture Guild. They do have a logo that we are able to use. I am an expert trouble shooting person and install primarily LED under cabinet lighting, flat screen televisions and recessed lighting. Services are very affordable. Pinecrest Electrical Service is not the company name.
Updates

Thank you for all of the great submissions. I do have one in mind so far. L.E.D.'s are different from the lamps shown on all of the cards. Shown is an incandescent or compact fluorescent lamp. Both will be obsolete before long. Please include my e-mail address hmarlo@quillpost.net on the card. This is not for your personal use. Thank you again.

I am still waiting for someone to get rid of the CFL lamps on the card and show me an LED. What's up?

Industry/Entity Type

Electrical

Contact Information for Business Card

Harold Marlo, Pinecrest Electrical Sevice, Electrical License #QR58419362, 352-555-0187, National Fixture Guild Master Beacon Fellow, 30 years Experience,

Requirements
Nice to have
• I do not have the NFG logo but would like to on the card along with something indicating electrical work.

```html
<!DOCTYPE html>
<html lang="en">
<head>
<meta charset="utf-8">
<title>Harold Marlo – Business Card</title>
<link rel="stylesheet" href="https://fonts.googleapis.com/css2?family=Arimo:wght@400;700&display=swap">
<style>
  :root {
    --backdrop: #d6d1cd;
    --backdrop-light: #e4e0dc;
    --ink: #141414;
    --paper: #ffffff;
    --muted: #8a8a8a;
    --front-text: #e9e9e9;
    --front-muted: #9a9a9a;
  }
  * { box-sizing: border-box; margin: 0; padding: 0; }
  html, body {
    width: 1200px;
    height: 675px;
    overflow: hidden;
  }
  body {
    background: radial-gradient(ellipse at 60% 30%, var(--backdrop-light), var(--backdrop));
    font-family: "Arimo", Arial, sans-serif;
    position: relative;
  }
  .card {
    position: absolute;
    top: 188px;
    width: 525px;
    height: 300px;
    box-shadow: 0 6px 18px rgba(0,0,0,0.18);
  }

  /* Front side */
  .card-front {
    left: 50px;
    background: var(--ink);
    color: var(--front-text);
  }
  .guild-mark {
    position: absolute;
    top: 108px;
    left: 0;
    right: 0;
    display: flex;
    justify-content: center;
    align-items: center;
    gap: 10px;
  }
  .guild-mark .square {
    width: 12px;
    height: 12px;
    background: var(--front-text);
  }
  .guild-mark .guild-name {
    font-size: 22px;
    font-weight: 400;
    letter-spacing: 1px;
    color: var(--front-text);
  }
  .front-tagline {
    position: absolute;
    bottom: 48px;
    left: 0;
    right: 0;
    text-align: center;
    font-size: 13px;
    letter-spacing: 0.5px;
    color: var(--front-muted);
  }

  /* Back side */
  .card-back {
    left: 625px;
    background: var(--paper);
    color: var(--ink);
  }
  .name-bar {
    position: absolute;
    left: 0;
    top: 50px;
    width: 18px;
    height: 58px;
    background: var(--ink);
  }
  .holder {
    position: absolute;
    left: 34px;
    top: 52px;
  }
  .holder-name {
    font-size: 27px;
    font-weight: 400;
    letter-spacing: 0.3px;
    line-height: 1;
  }
  .holder-role {
    margin-top: 6px;
    font-size: 9.5px;
    line-height: 1.35;
    color: var(--muted);
  }
  .contact-strip {
    position: absolute;
    right: 0;
    top: 180px;
    display: flex;
    flex-direction: column;
    align-items: flex-end;
    gap: 5px;
  }
  .contact-row {
    display: flex;
    align-items: stretch;
    gap: 3px;
  }
  .contact-row .tick {
    width: 5px;
    background: var(--ink);
  }
  .contact-row .band {
    background: var(--ink);
    color: var(--paper);
    font-size: 12px;
    line-height: 1;
    letter-spacing: 0.4px;
    white-space: nowrap;
    height: 22px;
    padding: 0 14px 0 8px;
    display: flex;
    align-items: center;
    gap: 8px;
  }
  .phone-band { width: 150px; }
  .email-band { width: 195px; }
  .license-band { width: 220px; }
  .contact-row svg { width: 11px; height: 11px; fill: var(--paper); flex: none; }
</style>
</head>
<body>
  <section class="card card-front">
    <div class="guild-mark">
      <span class="square"></span>
      <span class="guild-name">National Fixture Guild</span>
    </div>
    <p class="front-tagline">Pinecrest Electrical Service</p>
  </section>

  <section class="card card-back">
    <span class="name-bar"></span>
    <div class="holder">
      <h1 class="holder-name">Harold Marlo</h1>
      <p class="holder-role">National Fixture Guild<br>Master Beacon Fellow, 30 Years Experience</p>
    </div>
    <div class="contact-strip">
      <div class="contact-row">
        <span class="tick"></span>
        <span class="band phone-band">
          <svg viewBox="0 0 24 24" aria-hidden="true"><path d="M6.6 10.8a15.1 15.1 0 0 0 6.6 6.6l2.2-2.2c.3-.3.7-.4 1-.2 1.1.4 2.3.6 3.6.6.6 0 1 .4 1 1V20c0 .6-.4 1-1 1A17 17 0 0 1 3 4c0-.6.4-1 1-1h3.5c.6 0 1 .4 1 1 0 1.3.2 2.5.6 3.6.1.3 0 .7-.2 1z"/></svg>
          352 555 0187
        </span>
      </div>
      <div class="contact-row">
        <span class="tick"></span>
        <span class="band email-band">
          <svg viewBox="0 0 24 24" aria-hidden="true"><path d="M2 5h20v14H2zm2 2v.4l8 5 8-5V7zm0 2.8V17h16V9.8l-8 5z"/></svg>
          hmarlo@quillpost.net
        </span>
      </div>
      <div class="contact-row">
        <span class="tick"></span>
        <span class="band license-band">Electrical License #QR58419362</span>
      </div>
    </div>
  </section>
</body>
</html>
```